BRIGHT COLORFUL + 55 FAMILY HISTORY BROCHURE 11 x 17 bifold

11 x 17 Bifold Flyer I have given you the Layout I just need you to make it Pretty

YOU DO NOT NEED TO FOLLOW MY LAYOUT, You can but dont have too

Target Market(s)

55 year old consumers, who could choose our service of Hereditary Cancer Screening

Industry/Entity Type

Health And Wellness

Requirements
Must have
• Must be appealing to Grand Parents, must make them want to test , show lots of pictures of grand children, YOU DO NOT NEED TO FOLLOW MY LAYOUT , You can but dont have too
Nice to have
• use our colors of our logo , YOU DO NOT NEED TO FOLLOW MY LAYOUT , You can but dont have too
Should not have
• YOU DO NOT NEED TO FOLLOW MY LAYOUT, You can but dont have too

```html
<!DOCTYPE html>
<html lang="en">
<head>
<meta charset="utf-8">
<title>Hereditary Cancer Screening – Bifold Brochure</title>
<link href="https://fonts.googleapis.com/css2?family=Tinos:ital,wght@0,400;0,700;1,400;1,700&display=swap" rel="stylesheet">
<style>
  :root{
    --navy:#1b2463;
    --navy-deep:#141a4a;
    --green:#7cb82f;
    --paper:#ffffff;
    --page-bg:#e4e4e6;
    --ink:#2a2f55;
    --body:#3c3f55;
    --faint:#d9dbe6;
  }
  *{box-sizing:border-box;margin:0;padding:0}
  html,body{width:1200px;height:2500px;overflow:hidden}
  body{background:var(--page-bg);font-family:"Tinos","Times New Roman",serif;color:var(--ink)}
  .canvas{position:relative;width:1200px;height:2500px;padding:60px 50px;display:flex;flex-direction:column;gap:70px}
  .spread{position:relative;width:1100px;height:712px;display:flex;background:var(--paper);box-shadow:0 10px 30px rgba(0,0,0,.15)}
  .panel{position:relative;width:550px;height:712px;overflow:hidden}
  .panel + .panel{border-left:1px solid #e6e6ea}
  .photo{position:absolute;display:block}
  .wave{position:absolute;left:0;width:550px}
  .brand{position:absolute;display:flex;align-items:center;gap:7px;font-weight:700;font-size:15px;color:var(--navy);letter-spacing:.5px;text-transform:uppercase;z-index:2}
  .brand .dot{width:18px;height:18px;border-radius:50%;background:var(--green)}
  .brand.light{color:#fff}
  .watermark{position:absolute;border-radius:50%;border:14px solid var(--faint);opacity:.55;z-index:0}

  /* front cover */
  .cover-title{position:absolute;left:0;right:0;top:352px;text-align:center;font-size:36px;color:var(--navy);z-index:2}
  .cover-tagline{position:absolute;left:0;right:0;top:398px;text-align:center;font-size:21px;font-style:italic;color:var(--navy);z-index:2}
  .cover-question{position:absolute;left:40px;top:490px;width:245px;font-size:15px;line-height:1.35;color:var(--navy);z-index:2}
  .hands-photo{right:0;bottom:0;width:250px;height:200px;border-top-left-radius:120px 60px}
  .gift-line{position:absolute;right:22px;bottom:28px;width:170px;text-align:center;font-size:17px;font-style:italic;color:#fff;line-height:1.15;z-index:2}

  /* back panel */
  .back-headline{position:absolute;left:0;right:0;top:250px;text-align:center;font-size:24px;font-weight:700;font-style:italic;color:var(--navy);line-height:1.15}
  .thumbs{position:absolute;top:340px;left:60px;right:60px;display:flex;justify-content:space-between}
  .thumbs .photo{position:static;width:195px;height:110px;border:3px solid #fff;box-shadow:0 2px 6px rgba(0,0,0,.25)}
  .back-band{position:absolute;left:0;bottom:0;width:550px;height:250px;background:var(--navy)}
  .back-band .copy{position:absolute;left:30px;top:46px;width:400px;color:#fff;font-size:12.5px;line-height:1.4}
  .back-band .copy p + p{margin-top:8px}
  .web{position:absolute;font-size:11px;color:#fff;letter-spacing:.3px}

  /* inside */
  .inside-lead{position:absolute;left:30px;right:30px;top:262px;text-align:center;font-size:15px;font-weight:700;font-style:italic;color:var(--navy);line-height:1.3}
  .inside-body{position:absolute;left:34px;right:34px;font-size:12.5px;line-height:1.42;color:var(--body);text-align:justify;z-index:2}
  .inside-body p + p{margin-top:9px}
  .inside-head{position:absolute;left:30px;right:30px;top:318px;text-align:center;font-size:17px;color:var(--navy);line-height:1.25}
  .inside-head strong{font-weight:700}
  .web.dark{color:var(--navy)}
</style>
</head>
<body>
<main class="canvas">

  <section class="spread spread-outside">
    <article class="panel panel-back">
      <div class="photo" role="img" aria-label="Photo of a grandfather laughing as his granddaughter kisses his cheek" style="left:0;top:0;width:550px;height:235px;background:linear-gradient(120deg,#c9ccd6,#efe8e3 55%,#d8cfc6)"></div>
      <svg class="wave" style="top:205px" height="40" viewBox="0 0 550 40" preserveAspectRatio="none">
        <path d="M0 18 Q275 42 550 10 L550 40 L0 40Z" fill="#fff"/>
        <path d="M0 18 Q275 42 550 10" fill="none" stroke="var(--navy)" stroke-width="4"/>
      </svg>
      <h2 class="back-headline">DOES CANCER Run in Your Family?<br>A Simple Swab Could SAVE a Family Members LIFE</h2>
      <div class="thumbs">
        <div class="photo" role="img" aria-label="Photo of a grandmother hugging two grandchildren" style="background:linear-gradient(135deg,#6b5148,#b7927d)"></div>
        <div class="photo" role="img" aria-label="Photo of a grandmother smiling beside her grandchild" style="background:linear-gradient(135deg,#e9ddd1,#9fb4c9)"></div>
      </div>
      <div class="back-band">
        <svg class="wave" style="top:-22px" height="40" viewBox="0 0 550 40" preserveAspectRatio="none">
          <path d="M0 24 Q275 0 550 22 L550 40 L0 40Z" fill="var(--navy)"/>
          <path d="M0 24 Q275 0 550 22" fill="none" stroke="var(--green)" stroke-width="4"/>
        </svg>
        <div class="copy">
          <p>Your decision now will affect you, and it will also impact your family. Share your results and help the ones you love plan ahead.</p>
          <p>A simple test can show whether you carry inherited changes linked to certain cancers. Early answers give your family time to act.</p>
        </div>
        <span class="web" style="left:30px;bottom:22px">www.kinshipscreening.com</span>
        <div class="brand light" style="right:28px;bottom:20px"><span class="dot"></span>Kindred Health Group</div>
      </div>
    </article>

    <article class="panel panel-front">
      <div class="photo" role="img" aria-label="Photo of three generations of a family smiling together outdoors" style="left:0;top:0;width:550px;height:330px;background:linear-gradient(160deg,#d9e2a6,#e8d3b8 45%,#b9c4cf)"></div>
      <div class="watermark" style="left:190px;top:330px;width:170px;height:170px"></div>
      <svg class="wave" style="top:290px" height="60" viewBox="0 0 550 60" preserveAspectRatio="none">
        <path d="M0 40 Q260 10 550 30 L550 60 L0 60Z" fill="#fff"/>
        <path d="M0 40 Q260 10 550 30" fill="none" stroke="var(--navy)" stroke-width="5"/>
        <path d="M0 48 Q260 18 550 38" fill="none" stroke="var(--green)" stroke-width="2"/>
      </svg>
      <h1 class="cover-title">Hereditary Cancer Screening</h1>
      <p class="cover-tagline">"The Test You Take For Them"</p>
      <svg class="wave" style="top:455px" height="30" viewBox="0 0 550 30" preserveAspectRatio="none">
        <path d="M0 26 Q300 0 550 12" fill="none" stroke="var(--green)" stroke-width="3"/>
      </svg>
      <p class="cover-question">Will You give Your loved ones the information to Beat Cancer in their lives? Knowing is better than not knowing. Knowledge is Power</p>
      <div class="brand" style="left:40px;top:625px"><span class="dot"></span>Kindred Health Group</div>
      <div class="photo hands-photo" role="img" aria-label="Photo of a grandparent's hand holding a small child's finger over green grass" style="background:linear-gradient(135deg,#c9b08f,#7f9a45 60%,#58742c)"></div>
      <p class="gift-line">Give Them the Gift of Knowledge</p>
    </article>
  </section>

  <section class="spread spread-inside">
    <article class="panel panel-inside-left">
      <div class="photo" role="img" aria-label="Photo of a grandmother and mother holding a sleeping baby" style="left:0;top:0;width:550px;height:245px;background:linear-gradient(120deg,#f2e6dc,#d9b9a2 55%,#b98d72)"></div>
      <svg class="wave" style="top:222px" height="34" viewBox="0 0 550 34" preserveAspectRatio="none">
        <path d="M0 10 Q275 36 550 14 L550 34 L0 34Z" fill="#fff"/>
        <path d="M0 10 Q275 36 550 14" fill="none" stroke="var(--navy)" stroke-width="4"/>
      </svg>
      <p class="inside-lead">A Positive result, or Finding a mutation, Does Not Mean You Will Get Cancer. It Means You and Your Family Can Plan Ahead.</p>
      <div class="watermark" style="left:30px;top:530px;width:140px;height:140px"></div>
      <div class="inside-body" style="top:330px">
        <p>Genetic testing looks for inherited changes in genes that can raise the risk of some cancers. The test uses a simple cheek swab taken at home, and results are reviewed by trained specialists who explain what they mean for you.</p>
        <p>Many families share more than stories and traditions. They may also share a higher risk for certain cancers. Knowing your status helps your doctor choose screening that fits your history.</p>
        <p>Your results can guide children and grandchildren too. When one person tests, relatives learn whether they should speak with their own doctor about testing and earlier checkups.</p>
      </div>
      <div class="brand" style="left:34px;bottom:26px"><span class="dot"></span>Kindred Health Group</div>
    </article>

    <article class="panel panel-inside-right">
      <div class="photo" role="img" aria-label="Photo of grandparents, parents and grandchildren posing together in a park" style="left:28px;top:28px;width:494px;height:250px;background:linear-gradient(150deg,#a9c46b,#dfe3c4 50%,#8fb4d6)"></div>
      <svg class="wave" style="top:270px" height="30" viewBox="0 0 550 30" preserveAspectRatio="none">
        <path d="M0 8 Q275 30 550 8" fill="none" stroke="var(--navy)" stroke-width="4"/>
      </svg>
      <h2 class="inside-head">There are many Known risk factors for Cancer.<br><strong>GENETICS and FAMILY HISTORY</strong><br>are Often Overlooked</h2>
      <div class="watermark" style="left:180px;top:555px;width:130px;height:130px"></div>
      <div class="inside-body" style="top:405px">
        <p>Genetic testing is done to determine whether family members share an inherited risk. If a close relative had cancer at a young age, testing may help you and your loved ones take action early.</p>
        <p>Who should consider testing? Anyone with several relatives on the same side of the family who had breast, ovarian, colon or prostate cancer, or a relative diagnosed before age fifty.</p>
        <p>There are many benefits to knowing. Results can lead to earlier screening, better choices and peace of mind, and they give your family the chance to protect the people they love most.</p>
      </div>
      <span class="web dark" style="left:34px;bottom:30px">www.kinshipscreening.com</span>
      <div class="brand" style="right:30px;bottom:24px"><span class="dot"></span>Kindred Health Group</div>
    </article>
  </section>

</main>
</body>
</html>
```